Web Design - Personal Item Tags Portal

web page designs need to be created for a new company that provides item tracking tags and lets users register and report stolen/found items.
The theme of the designs needs to be energetic and convey a sense of freedom and adventure - where the user does not have to worry about their items since they have all been "tagged".
the client likes parts of the site at: http://www.brisklayouts.example/
they like:
1. slider images at top of pages. large slider on front page. fixed smaller height picture on internal pages
2. fixed company message on left-hand-side
3. My Account button to be clear and stand out

other comments:
clean, simple
• brand focused
• will have clear call to actions
• will include a description of what and why
• will appeal to both males and females

sections that the website will have are:
Home
About Us
How it works
Why
Case Studies
Uses and Applications
Shop
Contact Us

please create 2 designs : 1 home page, 1 internal page

Final winner will also require HTML slicing to be done.
Updates

hi, i have now updated the images so they work. sorry!

Hi, looking at all the designs that are coming in, alot of them are great. Designers need to remember to make the register for an account button more prominent. Also, there should be a "report found" and "report lost" buttons on the front-page and should be prominent as well.

Thanks

Hi, the customer has come back with a few comments and modifications for the designs, if you are able to make some tweaks to your submissions, that will be great:

The client would like the designs to be modified to highlight 3 main actions:
1. Log In/Register
2. Find an Owner
3. Lost an Item

The home page shouldnt be too content heavy in terms of text, it should only have major highlight points of what the system does (the 3 points listed above). the inner page designs are OK to have more text though.

i will also upload some notes from the customer that can be used as a guide and also include the design styles which the customer likes (but is not entirely happy with).

uploaded image files (3) with customer feedback comments

Industry/Entity Type

It Company

```html
<!DOCTYPE html>
<html lang="en">
<head>
<meta charset="utf-8">
<title>Roamkeep – Home</title>
<link href="https://fonts.googleapis.com/css2?family=Bree+Serif&family=Titillium+Web:wght@300;400;600&display=swap" rel="stylesheet">
<style>
  :root{
    --navy:#16305b;
    --navy-deep:#0f2549;
    --nav-blue:#2c6cc2;
    --nav-active:#1f4f96;
    --hero-deep:#0b4a98;
    --hero-mid:#1f7ad6;
    --hero-light:#9cc4ea;
    --green:#3bb95a;
    --blue-btn:#3a93dc;
    --card-bg:#f7f7f7;
    --card-border:#dcdcdc;
    --text:#555;
    --heading:#333;
    --footer-bg:#d6d6d6;
    --footer-text:#777;
  }
  *{box-sizing:border-box;margin:0;padding:0}
  html,body{width:1200px;height:1143px;overflow:hidden;background:#fff}
  body{position:relative;font-family:"Titillium Web",sans-serif;color:var(--text)}
  .abs{position:absolute}
  h1,h2{font-weight:400}

  .site-header{left:0;top:0;width:1200px;height:90px;background:linear-gradient(180deg,var(--navy-deep),var(--navy))}
  .brand{left:150px;top:16px;display:flex;align-items:center;gap:12px;color:#fff}
  .brand-mark{width:46px;height:46px;border-radius:50%;border:2px solid #fff}
  .brand-text{font-family:"Bree Serif",serif;font-size:36px;line-height:38px}
  .brand-tagline{font-family:"Bree Serif",serif;font-size:14px;line-height:16px;text-align:right}
  .social{top:36px;width:17px;height:17px;border-radius:3px;background:#5b9bd8}
  .account-btn{left:961px;top:30px;width:131px;height:27px;border-radius:14px;background:var(--green);color:#fff;font-family:"Bree Serif",serif;font-size:11.5px;display:flex;align-items:center;justify-content:center;gap:10px}

  .main-nav{left:0;top:90px;width:1200px;height:46px;background:linear-gradient(180deg,#3479cf,var(--nav-blue));border-bottom:1px solid #235aa6}
  .nav-item{top:0;height:46px;line-height:46px;color:#fff;font-family:"Bree Serif",serif;font-size:14px;white-space:nowrap}
  .nav-item.active{background:var(--nav-active);width:94px;text-align:center}

  .hero{left:0;top:136px;width:1200px;height:354px;background:radial-gradient(ellipse 520px 420px at 930px 80px,var(--hero-light),transparent 75%),radial-gradient(ellipse 600px 380px at 620px 250px,var(--hero-mid),transparent 80%),linear-gradient(90deg,var(--hero-deep),#1767c0 60%,#4e93d8)}
  .hero-title{left:0;top:36px;width:1200px;text-align:center;color:#fff;font-size:38px;font-weight:600;line-height:44px}
  .hero-sub{left:0;top:80px;width:1200px;text-align:center;color:#fff;font-size:21px;font-weight:300;line-height:24px}
  .register-btn{left:446px;top:133px;width:307px;height:40px;border-radius:20px;background:var(--green);box-shadow:0 2px 4px rgba(0,0,0,.25);color:#fff;font-family:"Bree Serif",serif;font-size:19px;line-height:40px;text-align:center}
  .hero-products{left:402px;top:218px;width:514px;height:136px;border-radius:20px 20px 0 0;background:linear-gradient(90deg,#1b1b1b,#2a2a2a 45%,#6f90b5 70%,#c3ccd6)}

  .card{background:var(--card-bg);border:1px solid var(--card-border);box-shadow:0 1px 3px rgba(0,0,0,.12)}
  .card-title{font-size:22px;font-weight:400;color:var(--heading);line-height:26px}
  .card-copy{font-size:11.5px;line-height:14px}
  .action-card{top:509px;width:316px;height:136px;text-align:center}
  .action-card .card-title{margin-top:14px}
  .action-card .card-copy{margin:8px 18px 0}
  .blue-btn{position:absolute;left:92px;top:91px;width:132px;height:28px;border-radius:14px;background:var(--blue-btn);color:#fff;font-family:"Bree Serif",serif;font-size:13px;line-height:28px;text-align:center}
  .grey-btn{height:28px;border-radius:14px;border:1px solid #ccc;background:linear-gradient(#fff,#e9e9e9);color:#444;font-family:"Bree Serif",serif;font-size:13px;line-height:26px;text-align:center}

  .why-title{left:141px;top:668px;font-size:33px;font-weight:600;color:var(--heading);line-height:44px}
  .why-copy{left:141px;width:640px;font-size:11.5px;line-height:14px}

  .testimonial{left:141px;top:881px;width:316px;height:171px}
  .uses{left:475px;top:881px;width:316px;height:171px}
  .portrait{left:15px;top:70px;width:68px;height:59px;background:linear-gradient(135deg,#888,#2a2a2a)}
  .quote-mark{font-family:"Bree Serif",serif;font-size:36px;color:#aaa;line-height:30px}
  .dot{top:152px;width:13px;height:13px;border-radius:50%;border:1px solid #aaa;background:#fff}
  .dot.on{background:var(--green);border-color:var(--green)}
  .use-item{left:24px;width:285px;display:flex;gap:8px}
  .use-item strong{display:block;color:#333;font-size:11.5px;font-weight:600}

  .sidebar{left:808px;top:508px;width:249px;height:544px}
  .sidebar-inner{left:6px;top:33px;width:237px;height:486px;background:#fff;border:1px solid #e2e2e2}
  .item{left:0;width:237px;text-align:center}
  .item-title{font-size:13.5px;font-weight:600;color:#333}
  .item-copy{font-size:11.5px;line-height:14px;margin:6px 20px 0}

  .site-footer{left:0;top:1079px;width:1200px;height:64px;background:var(--footer-bg);font-family:"Bree Serif",serif;font-size:10.5px;color:var(--footer-text);text-align:center}
</style>
</head>
<body>
  <header class="site-header abs">
    <div class="brand abs">
      <span class="brand-mark"></span>
      <div>
        <div class="brand-text">Roamkeep</div>
        <div class="brand-tagline">. . . travel light</div>
      </div>
    </div>
    <span class="social abs" style="left:862px"></span>
    <span class="social abs" style="left:889px"></span>
    <span class="social abs" style="left:915px"></span>
    <a class="account-btn abs">
      <svg width="10" height="12" viewBox="0 0 10 12"><rect x="1" y="5" width="8" height="7" rx="1" fill="#fff"/><path d="M3 5V3a2 2 0 0 1 4 0v2" stroke="#fff" stroke-width="1.5" fill="none"/></svg>
      My Account
    </a>
  </header>

  <nav class="main-nav abs">
    <span class="nav-item active abs" style="left:142px">Home</span>
    <span class="nav-item abs" style="left:258px">About Us</span>
    <span class="nav-item abs" style="left:362px">How it works</span>
    <span class="nav-item abs" style="left:488px">Why</span>
    <span class="nav-item abs" style="left:565px">Case Studies</span>
    <span class="nav-item abs" style="left:695px">Uses and Applications</span>
    <span class="nav-item abs" style="left:878px">Shop</span>
    <span class="nav-item abs" style="left:967px">Contact Us</span>
  </nav>

  <section class="hero abs">
    <h1 class="hero-title abs">Stolen Items can be found easily</h1>
    <p class="hero-sub abs">You can report any lost items here</p>
    <a class="register-btn abs">Register for an account</a>
    <div class="hero-products abs" role="img" aria-label="Camera, smartphone and laptop product photo"></div>
  </section>

  <div class="card action-card abs" style="left:141px">
    <h2 class="card-title">Have you found any items</h2>
    <p class="card-copy">Ut wisi enim ad minim veniam, quis nostrud exerci tation-suscipit lobortis nisl ut aliquip ex ea commodo</p>
    <a class="blue-btn">Report found</a>
  </div>
  <div class="card action-card abs" style="left:475px">
    <h2 class="card-title">Have you lost any items</h2>
    <p class="card-copy">Ut wisi enim ad minim veniam, quis nostrud exerci tation ullamcorper suscipit lobortis nisl ut aliquip</p>
    <a class="blue-btn">Report lost</a>
  </div>

  <h2 class="why-title abs">Why we are better</h2>
  <p class="why-copy abs" style="top:733px">Ut wisi enim ad minim veniam, quis nostrud exerci tation ullamcorper suscipit lobortis nisl ut aliquip ex ea commodo consequat. Duis autem vel eum iriure dolor in hendrerit in vulputate velit esse molestie consequat,</p>
  <p class="why-copy abs" style="top:774px">vel illum dolore eu feugiat nulla facilisis at vero eros et accumsan et iusto odio dignissim qui blandit praesent luptatum zzril delenit augue duis dolore te feugait nulla facilisi.</p>
  <a class="grey-btn abs" style="left:141px;top:826px;width:95px">More</a>

  <div class="card testimonial abs">
    <h2 class="card-title abs" style="left:14px;top:13px">What People say!</h2>
    <div class="portrait abs" role="img" aria-label="Customer portrait photo"></div>
    <span class="quote-mark abs" style="left:91px;top:50px">&ldquo;</span>
    <p class="card-copy abs" style="left:115px;top:62px;width:190px">Ut wisi enim ad minim veniam, quis nostrud exerci tation ullamcorper suscipit lobortis nisl ut aliquip ex ea commodo consequat.</p>
    <p class="abs" style="left:115px;top:118px;font-size:13px;line-height:16px;color:#333">Owen Marsh - Portland</p>
    <span class="quote-mark abs" style="left:277px;top:118px">&rdquo;</span>
    <span class="dot on abs" style="left:255px"></span>
    <span class="dot abs" style="left:275px"></span>
    <span class="dot abs" style="left:295px"></span>
  </div>

  <div class="card uses abs">
    <h2 class="card-title abs" style="left:36px;top:14px">Uses &amp; Applications</h2>
    <div class="use-item abs" style="top:58px">
      <svg width="8" height="10" viewBox="0 0 8 10" style="margin-top:3px;flex:none"><path d="M0 5h6M3 2l3 3-3 3" stroke="#888" stroke-width="1.2" fill="none"/></svg>
      <p class="card-copy"><strong>praesent luptatum</strong>Typi non habent claritatem insitam; est usus legentis in iis qui facit</p>
    </div>
    <div class="use-item abs" style="top:111px">
      <svg width="8" height="10" viewBox="0 0 8 10" style="margin-top:3px;flex:none"><path d="M0 5h6M3 2l3 3-3 3" stroke="#888" stroke-width="1.2" fill="none"/></svg>
      <p class="card-copy"><strong>praesent luptatum</strong>Typi non habent claritatem insitam; est usus legentis in iis qui facit</p>
    </div>
  </div>

  <aside class="card sidebar abs">
    <h2 class="abs" style="left:7px;top:7px;font-size:17px;color:#333">Latest Items</h2>
    <div class="sidebar-inner abs">
      <div class="abs" style="left:48px;top:24px;width:123px;height:97px;background:linear-gradient(160deg,#2f6fc2,#0d2c5a 55%,#b9bec4 56%,#e3e5e8)" role="img" aria-label="Laptop product photo"></div>
      <div class="item abs" style="top:140px">
        <p class="item-title">imperdiet doming</p>
        <p class="item-copy">Typi non habent claritatem insitam; est usus legentis in iis qui facit</p>
      </div>
      <a class="grey-btn abs" style="left:71px;top:204px;width:94px">Shop now</a>
      <div class="abs" style="left:95px;top:251px;width:48px;height:96px;border-radius:8px;background:linear-gradient(180deg,#222,#3b5f8f 30%,#2a4a70 75%,#111)" role="img" aria-label="Smartphone product photo"></div>
      <div class="item abs" style="top:378px">
        <p class="item-title">imperdiet doming</p>
        <p class="item-copy">Typi non habent claritatem insitam; est usus legentis in iis qui facit</p>
      </div>
      <a class="grey-btn abs" style="left:71px;top:442px;width:94px">Shop Now</a>
    </div>
    <span class="abs" style="left:14px;top:524px;font-size:11.5px;color:#333">View all</span>
  </aside>

  <footer class="site-footer abs">
    <p style="margin-top:18px">Home &nbsp;|&nbsp; About Us &nbsp;|&nbsp; How it works &nbsp;|&nbsp; Why &nbsp;|&nbsp; Case Studies &nbsp;|&nbsp; Uses and Applications &nbsp;|&nbsp; Shop &nbsp;|&nbsp; Contact Us</p>
    <p style="margin-top:1px">@Copyrights 2013 roamkeep.example &nbsp;|&nbsp; All rights reserved</p>
  </footer>
</body>
</html>
```